Business card for IT company

Looking for a business card for an IT company providing server, network, and application support to medium businesses. Company name is Calderwick Systems. Website is www.calderwicksystems.example, would like to use the green color that is on the homepage. Prefer design to be done in Illustrator. Please, only DESIGNERS apply - no PHP programmers attempting to do design. Thank you

Industry/Entity Type

Information Technology

Requirements
Must have
• Green
Should not have
• Template designs, or designs done by non-designer type people

```html
<!DOCTYPE html>
<html lang="en">
<head>
<meta charset="utf-8">
<title>Calderwick Systems — Business Card</title>
<link rel="stylesheet" href="https://fonts.googleapis.com/css2?family=Quicksand:wght@400;500&display=swap">
<style>
  :root {
    --stage: #1c1917;
    --brand-green: #a3ff2c;
    --card-dark: #2b2b2b;
    --ink-light: #ffffff;
    --label: #f2f2f2;
    --shadow: rgba(0, 0, 0, 0.45);
  }
  * { box-sizing: border-box; margin: 0; padding: 0; }
  html, body {
    width: 1200px;
    height: 1200px;
    overflow: hidden;
    background: var(--stage);
    font-family: "Quicksand", "Century Gothic", sans-serif;
  }
  .presentation { position: relative; width: 1200px; height: 1200px; }

  .side-label {
    position: absolute;
    right: 978px;
    font-size: 44px;
    font-weight: 400;
    color: var(--label);
    letter-spacing: 1px;
    line-height: 1;
  }
  .side-label--front { top: 130px; }
  .side-label--back { top: 612px; }

  .card {
    position: absolute;
    left: 247px;
    width: 706px;
    height: 425px;
    box-shadow: 2px 4px 10px var(--shadow);
    overflow: hidden;
  }
  .card--front { top: 132px; background: var(--brand-green); }
  .card--back { top: 614px; background: var(--card-dark); }

  /* Front */
  .brand-disc {
    position: absolute;
    left: 293px;
    top: 108px;
    width: 120px;
    height: 120px;
    border-radius: 50%;
    background: var(--ink-light);
  }
  .brand-name {
    position: absolute;
    left: 0;
    right: 0;
    top: 246px;
    text-align: center;
    color: var(--ink-light);
    font-size: 30px;
    font-weight: 500;
    letter-spacing: 1px;
    text-transform: uppercase;
  }

  /* Back */
  .company-heading {
    position: absolute;
    left: 61px;
    top: 60px;
    color: var(--ink-light);
    font-size: 21px;
    font-weight: 500;
    letter-spacing: 0.5px;
    text-transform: uppercase;
  }
  .heading-rule {
    position: absolute;
    left: 61px;
    top: 96px;
    width: 222px;
    height: 4px;
    background: var(--ink-light);
  }
  .contact-list { list-style: none; }
  .contact-item {
    position: absolute;
    left: 61px;
    height: 30px;
    display: flex;
    align-items: center;
    color: var(--ink-light);
    font-size: 21px;
    font-weight: 500;
  }
  .contact-item--email { top: 139px; }
  .contact-item--phone { top: 194px; }
  .contact-item--web { top: 247px; }
  .contact-icon {
    width: 26px;
    height: 26px;
    margin-right: 17px;
    fill: var(--ink-light);
    flex-shrink: 0;
  }
</style>
</head>
<body>
<main class="presentation">
  <span class="side-label side-label--front">Front</span>
  <section class="card card--front" aria-label="Card front">
    <div class="brand-disc"></div>
    <p class="brand-name">Calderwick Systems</p>
  </section>

  <span class="side-label side-label--back">Back</span>
  <section class="card card--back" aria-label="Card back">
    <h1 class="company-heading">Calderwick Systems</h1>
    <div class="heading-rule"></div>
    <ul class="contact-list">
      <li class="contact-item contact-item--email">
        <svg class="contact-icon" viewBox="0 0 26 26" aria-hidden="true">
          <path d="M1 6h24v15H1z M2.5 7.5 13 15 23.5 7.5" fill="none" stroke="#fff" stroke-width="2" stroke-linejoin="round"/>
          <path d="M1 6h24L13 14.5z"/>
        </svg>
        info@calderwicksystems.example
      </li>
      <li class="contact-item contact-item--phone">
        <svg class="contact-icon" viewBox="0 0 26 26" aria-hidden="true">
          <path d="M6.5 2.5l3.6 4.6-2.3 2.6c1.3 3.3 4 6.2 7.4 7.8l2.5-2.3 4.8 3.4-1.8 4.1C12.5 22.7 3.6 13.4 3 5z"/>
        </svg>
        5550142876
      </li>
      <li class="contact-item contact-item--web">
        <svg class="contact-icon" viewBox="0 0 26 26" aria-hidden="true">
          <circle cx="13" cy="13" r="11" fill="none" stroke="#fff" stroke-width="2"/>
          <path d="M8 5c2 1 3 3 2 5s-3 1-3 4 3 3 3 6c-2-1-6-3-6-8 0-3 2-6 4-7zM16 4c3 1 6 4 6 8-2 0-3-1-4 0s0 3-1 4-3 0-3-2 1-3 0-4-2-1-2-3 2-3 4-3z"/>
        </svg>
        www.calderwicksystems.example
      </li>
    </ul>
  </section>
</main>
</body>
</html>
```